Talent Harbor Posts - Built for the Industry, by the Industry.

Looking for an email marketing Infographic I can send out via email to target Recruitment Firms letting them know we are launched! As of January 7th VORANTE is no longer allowing Recruitment Firms to post on their site unless you pay thousands of dollars a month. We are launching a site just for Recruiters to showcase their jobs. I have attached the almost completed website and a mocked up version of a simple infographic but we are looking for a WOW design that can get emailed out to 1000's of Recruitment Firms and they will just have to click the image to be taken to our site. I have added the colors and raleway - medium is the font on our site. Blue RGB: 8/113/182 Navy RGB: 27/32/48

Recruitment Firms Across Canada and the USA

• WOW Factor, use of our Brand and Colours - raleway - medium is the font on our site. Blue RGB: 8/113/182 Navy RGB: 27/32/48. Our Logo and I have also attached our Landing Page ... down below.
• You can use "It's Time for Something New" or I'd be open to other ideas and taglines ... I'd like to see No Sponsored Jobs / No Pay-Per-Click / Flat Rates Only ...
• Our tagline is also - Built for the Industry, by the Industry"

```html
<!DOCTYPE html>
<html lang="en">
<head>
<meta charset="utf-8">
<title>Talent Harbor Posts – Launch Email</title>
<link rel="stylesheet" href="https://fonts.googleapis.com/css2?family=Montserrat:wght@400;700;800&family=Poppins:wght@400;500;600&display=swap">
<style>
  :root {
    --bg: #353441;
    --rule: #5e5d69;
    --white: #ffffff;
    --muted: #c9c8d0;
    --blue: #2f9bf0;
    --orange: #f7961f;
    --photo-dark: #2a2a2e;
    --photo-mid: #6b6b70;
    --photo-light: #9d9da2;
    --social-one: #2a5fc0;
    --social-two: #58c6ef;
    --social-three: #1f7db9;
  }
  * { margin: 0; padding: 0; box-sizing: border-box; }
  html, body { width: 1200px; height: 2688px; overflow: hidden; }
  body {
    background: var(--bg);
    font-family: "Poppins", sans-serif;
    color: var(--white);
    position: relative;
  }
  .email { position: relative; width: 1200px; height: 2688px; }
  .top-nav {
    position: absolute; top: 62px; left: 8px; right: 18px;
    display: flex; justify-content: space-between; font-size: 29px;
  }
  .top-nav .links span.sep { margin: 0 26px; }
  .top-nav .browser-link { color: var(--blue); }
  .rule { position: absolute; left: 20px; right: 20px; height: 2px; background: var(--rule); }
  .brand {
    position: absolute; top: 200px; left: 0; right: 0;
    display: flex; align-items: center; justify-content: center; gap: 30px;
  }
  .brand-mark { width: 110px; height: 110px; border-radius: 50%; background: #e6e6e8; }
  .brand-name {
    font-family: "Poppins", sans-serif; font-weight: 500;
    font-size: 56px; letter-spacing: 3px; color: #e6e6e8;
  }
  .hero {
    position: absolute; top: 484px; left: 20px; width: 1160px; height: 1000px;
    background: radial-gradient(ellipse at 50% 70%, var(--photo-light) 0%, var(--photo-mid) 45%, var(--photo-dark) 100%);
  }
  .hero-kicker {
    position: absolute; top: 100px; left: 0; right: 0; text-align: center;
    font-family: "Montserrat", sans-serif; font-weight: 400; font-size: 60px;
  }
  .hero-title {
    position: absolute; top: 170px; left: 0; right: 0; text-align: center;
    font-family: "Montserrat", sans-serif; font-weight: 800; font-size: 118px; letter-spacing: -1px;
  }
  .perks {
    position: absolute; top: 1560px; left: 0; right: 0;
    display: flex; justify-content: center; gap: 26px;
    font-weight: 500; font-size: 35px; list-style: none;
  }
  .perks li { display: flex; align-items: center; gap: 14px; }
  .perks li::before {
    content: ""; width: 18px; height: 18px; border-radius: 50%; background: var(--blue);
  }
  .intro {
    position: absolute; top: 1700px; left: 36px; right: 28px;
    text-align: center; color: var(--muted); font-size: 27px; line-height: 34px;
  }
  .cta {
    position: absolute; top: 1892px; left: 262px; width: 680px; height: 98px;
    background: var(--orange); color: var(--white);
    display: flex; align-items: center; justify-content: center; gap: 22px;
    font-family: "Montserrat", sans-serif; font-weight: 700; font-size: 34px; letter-spacing: 4px;
    text-decoration: none;
  }
  .contact { position: absolute; top: 2124px; left: 0; right: 0; text-align: center; }
  .contact-label { font-size: 30px; letter-spacing: 1px; }
  .contact-url {
    font-family: "Montserrat", sans-serif; font-weight: 800;
    font-size: 46px; letter-spacing: 4px; margin-top: 4px;
  }
  .contact-lines { font-size: 28px; margin-top: 12px; }
  .contact-lines a { color: var(--blue); text-decoration: none; }
  .contact-lines .sep { margin: 0 22px; }
  .social {
    position: absolute; top: 2446px; left: 0; right: 0;
    display: flex; justify-content: center; gap: 16px;
  }
  .social a { width: 100px; height: 100px; border-radius: 50%; display: block; }
  .social .one { background: var(--social-one); }
  .social .two { background: var(--social-two); }
  .social .three { background: var(--social-three); }
</style>
</head>
<body>
<main class="email">
  <nav class="top-nav">
    <div class="links"><span>Post Job</span><span class="sep">|</span><span>Search Job</span></div>
    <span class="browser-link">View in Web Browser</span>
  </nav>
  <div class="rule" style="top:146px"></div>

  <header class="brand">
    <span class="brand-mark"></span>
    <span class="brand-name">TALENT HARBOR POSTS</span>
  </header>
  <div class="rule" style="top:392px"></div>

  <section class="hero" role="img" aria-label="Black and white photo of a woman pointing at a laptop showing the job board website, with a coffee cup on the desk">
    <p class="hero-kicker">ITS TIME FOR</p>
    <h1 class="hero-title">SOMETHING NEW</h1>
  </section>

  <ul class="perks">
    <li>NO SPONSORED JOB</li>
    <li>NO PAY PER CLICK</li>
    <li>FLAT RATES ONLY</li>
  </ul>

  <p class="intro">Let our vast network of recruiters connect you &nbsp;with your next opportunity. Work with our top recruiters to discover confidential, new and unadvertised jobs not seen anywhere.</p>

  <a class="cta" href="#">SHOW ME HOW IT WORKS
    <svg width="30" height="30" viewBox="0 0 30 30" aria-hidden="true"><path d="M3 15h22M15 5l10 10-10 10" fill="none" stroke="#fff" stroke-width="4.5" stroke-linecap="round" stroke-linejoin="round"/></svg>
  </a>

  <div class="rule" style="top:2088px"></div>

  <section class="contact">
    <p class="contact-label">VISIT US AT</p>
    <p class="contact-url">WWW.TALENTHARBORPOSTS.COM</p>
    <p class="contact-lines">PHONE: <a href="#">8888 .4417.2093</a><span class="sep">|</span>EMAIL: <a href="#">hello@talentharborposts.com</a></p>
  </section>

  <div class="rule" style="top:2358px"></div>

  <nav class="social">
    <a class="one" href="#" aria-label="Social link one"></a>
    <a class="two" href="#" aria-label="Social link two"></a>
    <a class="three" href="#" aria-label="Social link three"></a>
  </nav>
</main>
</body>
</html>
```